Visitenkarten für Familienunternehmen in den Bereichen Fliesen, Natursteine, Kaminöfen, Schwimmbäder und Whirlpools
Zielgruppe
Wir sind ein Familienunternehmen in dritter Generation und Spezialist für Fliesen, Natursteine, Kaminöfen, Schwimmbäder und Whirlpools. Professionell, kreativ und voller Leidenschaft begleiten wir unsere Kunden bei der Umsetzung ihrer Vorhaben. Von der persönlichen Beratung bis hin zur Ausführung profitieren unsere Kunden von qualifiziertem Fachpersonal und 60 Jahren Erfahrung. Unsere Zielgruppe sind Familien/Paare ab 35 Jahren, die Produkte höchster Qualität für Ihr Zuhause suchen.
Aufgabenstellung
Wir benötigen neue Visitenkarten, da wir ein neues Logo haben. Wir haben folgende Vorstellung:
Rückseite: Komplett schwarz bzw. dunkel (Farbton ähnlich DB703), mittig unser neues Logo in weiß.
Vorderseite: Auch hier Hintergrund schwarz, Logo in weiß, Name des Ansprechpartners samt Titel/Position, Firmenname, Adresse, Telefonnummer, eMail-Adresse und Social Media-Adresse. Des Weiteren sollte unser Portfolio aufgelistet sein (Fliesen, Natursteine, Kaminöfen, Schwimmbäder und Whirlpools). Alternativ können wir uns die Auflistung des Portfolios auch auf der Rückseite vorstellen. Alternativ können wir uns die Vorderseite auch in weiß mit schwarzer Schrift vorstellen.
Der Inhalt der Datei, welche am Ende erstellt wird, muss für unsere Druckerei editierbar sein (Schrift als Text, nicht als Pfad).
Ergänzung 25.03.2023:
Nachdem die ersten Design-Vorschläge eingetroffen sind, haben wir uns dazu entschieden, dass es eine Visitenkarte im Querformat sein soll. Vorder- und Rückseite vollen schwarz/dunkel sein.

```html
<!DOCTYPE html>
<html lang="de">
<head>
<meta charset="utf-8">
<title>Marmor-Brok Visitenkarte</title>
<link rel="stylesheet" href="https://fonts.googleapis.com/css2?family=Poppins:wght@300;400;700&family=Open+Sans:wght@400&display=swap">
<style>
  :root {
    --stage: #ececec;
    --card-dark: #161616;
    --band-light: #f2f2f2;
    --ink-dark: #1b1b1b;
    --paper: #ffffff;
    --paper-soft: #d6d6d6;
  }
  * { margin: 0; padding: 0; box-sizing: border-box; }
  html, body { width: 1200px; height: 720px; overflow: hidden; }
  body {
    background: var(--stage);
    font-family: "Poppins", sans-serif;
    position: relative;
  }
  .card {
    position: absolute;
    top: 185px;
    width: 540px;
    height: 350px;
    overflow: hidden;
    background: var(--card-dark);
    color: var(--paper);
    box-shadow: 0 2px 6px rgba(0,0,0,0.15);
  }
  .card--front { left: 40px; }
  .card--back { left: 620px; }

  .brand-name {
    font-family: "Poppins", sans-serif;
    font-weight: 700;
    letter-spacing: 0;
    color: var(--paper);
  }
  .card--front .brand-name {
    position: absolute;
    left: 34px; top: 34px;
    font-size: 40px;
    line-height: 1;
  }
  .card--back .brand-name {
    position: absolute;
    left: 0; right: 0; top: 50%;
    transform: translateY(-50%);
    text-align: center;
    font-size: 52px;
    line-height: 1;
  }

  .person { position: absolute; left: 34px; top: 170px; }
  .person__name { font-weight: 700; font-size: 27px; line-height: 1.1; }
  .person__role { font-weight: 300; font-size: 20px; line-height: 1.3; }

  .portfolio { position: absolute; left: 34px; top: 262px; width: 230px; }
  .portfolio__label { font-weight: 700; font-size: 15px; margin-bottom: 3px; }
  .portfolio__list { font-family: "Open Sans", sans-serif; font-size: 11px; line-height: 1.35; color: var(--paper-soft); }

  .contact {
    position: absolute;
    left: 318px; top: 40px;
    list-style: none;
    font-family: "Open Sans", sans-serif;
    font-size: 11.5px;
    line-height: 1.45;
    color: var(--paper-soft);
  }
  .contact__item { display: flex; gap: 8px; margin-bottom: 3px; }
  .contact__icon { width: 13px; height: 13px; flex: none; margin-top: 2px; color: var(--paper); }

  .social-band {
    position: absolute;
    right: 0; bottom: 0;
    width: 270px; height: 46px;
    background: var(--band-light);
    border-top-left-radius: 18px;
    display: flex;
    align-items: center;
    justify-content: space-evenly;
    color: var(--ink-dark);
    font-family: "Open Sans", sans-serif;
    font-size: 11.5px;
  }
  .social-band__handle { display: flex; align-items: center; gap: 7px; }
  .social-band__dot { width: 12px; height: 12px; border-radius: 50%; background: var(--ink-dark); }
</style>
</head>
<body>
  <section class="card card--front" aria-label="Vorderseite">
    <div class="brand-name">Brok</div>

    <div class="person">
      <div class="person__name">Timo Brok</div>
      <div class="person__role">Geschäftsführer</div>
    </div>

    <div class="portfolio">
      <div class="portfolio__label">Portfolio:</div>
      <div class="portfolio__list">Fliesen, Natursteine, Kaminöfen,<br>Schwimmbäder und Whirlpools</div>
    </div>

    <ul class="contact">
      <li class="contact__item">
        <svg class="contact__icon" viewBox="0 0 16 16" fill="none" stroke="currentColor" stroke-width="1.4"><path d="M8 15s5-5 5-9a5 5 0 0 0-10 0c0 4 5 9 5 9z"/><circle cx="8" cy="6" r="1.8"/></svg>
        <span>Marmor-Brok GmbH<br>Lindenweg 3<br>76829 Wiesental</span>
      </li>
      <li class="contact__item">
        <svg class="contact__icon" viewBox="0 0 16 16" fill="currentColor"><path d="M4 1.5l2 3-1.3 1.4a8 8 0 0 0 5.4 5.4L11.5 10l3 2-1 2.5C7 14.5 1.5 9 1.5 2.5z"/></svg>
        <span>0 61 23 - 45 67 00</span>
      </li>
      <li class="contact__item">
        <svg class="contact__icon" viewBox="0 0 16 16" fill="none" stroke="currentColor" stroke-width="1.4"><rect x="1.5" y="3.5" width="13" height="9"/><path d="M1.5 3.5l6.5 5 6.5-5"/></svg>
        <span>info@marmor-brok.de</span>
      </li>
      <li class="contact__item">
        <svg class="contact__icon" viewBox="0 0 16 16" fill="none" stroke="currentColor" stroke-width="1.3"><circle cx="8" cy="8" r="6.3"/><path d="M1.7 8h12.6M8 1.7c-3 3.5-3 9 0 12.6M8 1.7c3 3.5 3 9 0 12.6"/></svg>
        <span>www.marmor-brok.de</span>
      </li>
    </ul>

    <div class="social-band">
      <span class="social-band__handle"><span class="social-band__dot"></span>@marmorbrok</span>
      <span class="social-band__handle"><span class="social-band__dot"></span>@marmorbrok</span>
    </div>
  </section>

  <section class="card card--back" aria-label="Rückseite">
    <div class="brand-name">Brok</div>
  </section>
</body>
</html>
```